Female Vocalist Needs Design for Music Album

Hi, my name is Corinna Vashti and I need a design for my first album. It will be a Digipak, 4 panel (1tray) and disk. (I will be using pressforge to print the CDs. Please see http://www.pressforgeworks.example/templates/ for digipak template and design specs.)
The musical genre of this album is sacred/religious/gospel- solo mezzo soprano with solo piano accompaniment. The musical style is traditional with a few pieces that have a more contemporary feel.
I would like to see designs that have the following:
FRONT COVER (Panel 1):
Photo of the artist, name of the artist, and album title: Lift Up Your Lantern (see attached). Try to create the feeling that the artist is alone in the shadows and light from heaven is pouring down onto her face as she is crying out to God. Font for the artist name in a flowing script-like calligraphic handwriting.
BACK COVER (Panel 2):
Photo of the artist and the track list (see attached).
INSIDE PANEL (Panel 3 - Back side of Front Cover):
Dedication, Special Thank You, and Credits (see attached). May include a picture of the recording artist.
CD TRAY PANEL (Panel 4):
Background using the design elements and colors used throughout, but no photos of the artist.
CD DISK DESIGN:
Name of the artist and album title on background using design elements and colors used throughout, but no photos of the artist.
I would like to see some 'sophistication' (for lack of a better word) in the design. It may be elegantly simple, or more elaborate- something well thought out down to the choice of font style and placement. Please feel free to use your imagination and creativity. The final design should enhance the photo of the artist and go with the overall prayerful theme of the album title.
Attached are some design examples that I found interesting.
Updates
For those who did not get the album text, I just re posted the attachment. I apologize...I thought I had attached it, but apparently accidentally detached it when I was editing the brief. We added the track lengths and made a few corrections and additions to the album text. Please see the attached Word Document "Corinna Vashti Album Text" on the brief. Thank you.
Target Market(s)
Target market are Christians and people of faith.
Industry/Entity Type
Religious
Requirements
Must have
- For the front cover, please use photo P1140955. For the back cover, please use photo P1140515.
Nice to have
- Retouch the artist photo to remove any incidental blemishes. Remove any distracting elements like in the photo backgrounds, unless you think it goes with the design theme. Crop photos as necessary. Please use your best judgement on whether to keep the photo background or to enhance it, add on to it, or completely change the backgrounds and/or to add other design elements and ornamentation. If another background is used, make sure it does not clash with what the artist is wearing and there is still good contrast between the photo and the background. One idea could be to use a off-white/light grey background on the outside covers and red on the inside covers. Ornamentation should be light, translucent, and subtle.
Should not have
- The design should NOT include any religious symbols or icons such as crosses, fishes, doves, etc., and no cartoon-like clip art.

```html
<!DOCTYPE html>
<html lang="en">
<head>
<meta charset="utf-8">
<title>Corinna Vashti – Lift Up Your Lantern – Digipak Layout</title>
<link rel="stylesheet" href="https://fonts.googleapis.com/css2?family=Pinyon+Script&family=EB+Garamond:ital,wght@0,500;1,500;1,600&display=swap">
<style>
:root{
  --page:#ffffff;
  --leaf-deep:#4f6a2e;
  --leaf-mid:#8fb061;
  --leaf-mist:#d7e6c4;
  --mist:#eef4e4;
  --bark:#5b4a3a;
  --jacket-red:#c8233a;
  --hair:#1c1a1c;
  --cream:#f3ecc8;
  --ink:#2f3a1d;
  --disc:#dcebc6;
}
*{box-sizing:border-box;margin:0;padding:0}
html,body{width:1200px;height:1000px;overflow:hidden;background:var(--page)}
.spread{position:relative;width:1200px;height:1000px}
.panel{position:absolute;width:518px;height:468px;overflow:hidden}
.panel--front{left:70px;top:25px}
.panel--back{left:617px;top:25px}
.panel--inside{left:70px;top:508px;height:467px}
.panel--tray{left:617px;top:508px;height:467px}
.photo{position:absolute}
.ornament{position:absolute;border-radius:50%;opacity:.55}

/* front */
.front-photo{inset:0;background:
  radial-gradient(ellipse 30% 45% at 38% 40%, #c98f72 0%, rgba(201,143,114,0) 70%),
  radial-gradient(ellipse 35% 40% at 35% 95%, var(--jacket-red) 0%, rgba(200,35,58,0) 75%),
  radial-gradient(ellipse 30% 60% at 12% 45%, var(--hair) 0%, rgba(28,26,28,0) 80%),
  linear-gradient(90deg, #3e3a2c 0%, #6b5d4a 35%, var(--bark) 60%, var(--leaf-mid) 78%, #b9d38b 100%)}
.front-orn-top{right:-40px;top:-20px;width:220px;height:260px;background:radial-gradient(circle,var(--cream) 0%,rgba(243,236,200,0) 70%)}
.front-orn-bottom{left:-40px;bottom:-30px;width:200px;height:200px;background:radial-gradient(circle,var(--cream) 0%,rgba(243,236,200,0) 70%)}
.cover-title{position:absolute;right:22px;bottom:14px;text-align:right;color:#fbf8ee;text-shadow:0 1px 3px rgba(0,0,0,.55)}
.artist-name{font-family:"Pinyon Script",cursive;font-size:38px;line-height:1}
.album-title{font-family:"EB Garamond",serif;font-style:italic;font-size:29px;line-height:1.2;margin-top:2px}

/* back */
.back-bg{inset:0;background:linear-gradient(160deg,#f6f9ef 0%,var(--leaf-mist) 55%,#c3d8a6 100%)}
.back-photo{right:0;top:40px;width:270px;height:428px;background:
  radial-gradient(ellipse 30% 28% at 50% 40%, #d09a7e 0%, rgba(208,154,126,0) 75%),
  radial-gradient(ellipse 60% 30% at 60% 100%, var(--jacket-red) 0%, rgba(200,35,58,0) 80%),
  radial-gradient(ellipse 55% 60% at 55% 45%, var(--hair) 0%, rgba(28,26,28,0) 80%);
  border-radius:40% 0 0 0}
.back-orn{left:0;bottom:20px;width:170px;height:170px;background:radial-gradient(circle,var(--cream) 0%,rgba(243,236,200,0) 70%)}
.tracklist{position:absolute;left:16px;top:16px;list-style:none;font-family:"EB Garamond",serif;font-style:italic;font-weight:600;font-size:15.5px;line-height:19px;color:var(--ink)}
.tracklist .num{display:inline-block;width:16px;text-align:right;margin-right:5px}
.tracklist .cont{padding-left:21px}

/* inside */
.inside-bg{inset:0;background:linear-gradient(170deg,#f3f7ea 0%,var(--leaf-mist) 50%,#e6efd8 100%)}
.inside-orn{left:220px;top:310px;width:70px;height:50px;background:radial-gradient(circle,var(--cream) 0%,rgba(243,236,200,0) 70%)}
.credits{position:absolute;font-family:"EB Garamond",serif;font-style:italic;font-weight:600;font-size:8.3px;line-height:10.4px;color:var(--ink)}
.credits p{margin-bottom:6px}
.credits h2{font-family:"EB Garamond",serif;font-weight:500;font-style:normal;font-size:10px;letter-spacing:.3px;margin-bottom:3px}
.credits-left{left:10px;top:10px;width:252px}
.credits-right{left:266px;top:26px;width:244px}
.thanks-left{left:10px;top:350px;width:245px}
.thanks-right{left:266px;top:368px;width:244px}
.studio{margin-top:20px}

/* tray / disc */
.tray-bg{inset:0;background:linear-gradient(90deg,#e8eee0 0%,#f4f6ee 45%,#dfe6d4 80%,#c9cfbf 100%)}
.tray-orn-a{left:0;top:0;width:140px;height:140px;background:radial-gradient(circle,var(--cream) 0%,rgba(243,236,200,0) 70%)}
.tray-orn-b{right:0;top:0;width:130px;height:130px;background:radial-gradient(circle,var(--cream) 0%,rgba(243,236,200,0) 70%)}
.disc-svg{position:absolute;left:0;top:0}
.disc-title{position:absolute;left:30px;width:458px;top:88px;text-align:center;color:#fbfbf2}
.disc-title .artist-name{font-size:27px}
.disc-title .album-title{font-size:20px;margin-top:0}
</style>
</head>
<body>
<main class="spread">

  <section class="panel panel--front" aria-label="Front cover">
    <div class="photo front-photo" role="img" aria-label="Photo of the artist in a red jacket looking upward beside a tree trunk, sunlit greenery behind"></div>
    <div class="ornament front-orn-top" role="img" aria-label="Translucent cream flourish ornament"></div>
    <div class="ornament front-orn-bottom" role="img" aria-label="Translucent cream flourish ornament"></div>
    <div class="cover-title">
      <div class="artist-name">Corinna Vashti</div>
      <div class="album-title">Lift Up Your Lantern</div>
    </div>
  </section>

  <section class="panel panel--back" aria-label="Back cover">
    <div class="photo back-bg" role="img" aria-label="Soft misty woodland background in pale greens"></div>
    <div class="photo back-photo" role="img" aria-label="Portrait photo of the artist smiling, dark hair, red jacket"></div>
    <div class="ornament back-orn" role="img" aria-label="Translucent cream flourish ornament"></div>
    <ol class="tracklist">
      <li><span class="num">1.</span>Lift Up Your Lantern / Rock of Ages</li>
      <li><span class="num">2.</span>His Eye is On the Sparrow</li>
      <li><span class="num">3.</span>Give Them All to Jesus Medley</li>
      <li><span class="num">4.</span>Great is Thy Faithfulness / Day By Day</li>
      <li><span class="num">5.</span>There is a Fountain</li>
      <li><span class="num">6.</span>Are You Ready for Jesus to Come /</li>
      <li class="cont">Redemption Draweth Nigh</li>
      <li><span class="num">7.</span>A Quiet Place</li>
      <li><span class="num">8.</span>Midnight Cry</li>
      <li><span class="num">9.</span>The Holy City</li>
      <li><span class="num">10.</span>The Lord's Prayer</li>
    </ol>
  </section>

  <section class="panel panel--inside" aria-label="Inside panel">
    <div class="photo inside-bg" role="img" aria-label="Faded woodland background in pale greens"></div>
    <div class="ornament inside-orn" role="img" aria-label="Small cream flourish ornament"></div>
    <div class="credits credits-left">
      <h2>CREDITS:</h2>
      <p>Lift Up Your Lantern / Rock of Ages<br>Lift Up Your Lantern – Psalm 61:1-3<br>Rock of Ages – Words by Ambrose Kettleworth. Music by Silas Pennick.<br>Medley Arrangement by Dorian Vashti.</p>
      <p>His Eye is On the Sparrow<br>Words by Lavinia R. Holt. Music by Edwin J. Farrow.<br>Arranged by Teodor Almaren.</p>
      <p>Give Them All to Jesus Medley<br>Give Them All – Words and Music by Neal Corbin &amp; Hal Whitcombe Sr.<br>Down In My Heart – Words and Music by Milton Ashby Crane.<br>Into My Heart – Words and Music by Walter E. Prynne.<br>Medley Arrangement by Dorian Vashti.</p>
      <p>Great is Thy Faithfulness / Day By Day<br>Great is Thy Faithfulness – Words by Josiah Marlowe. Music by Henry L. Tabor.<br>Day By Day – Words and Music by Ingrid M. Solvang-Ek.<br>Medley Arrangement by Teodor Almaren.</p>
      <p>There is a Fountain<br>Words and Music by Nathaniel Brisco. Arranged by Dorian Vashti.</p>
    </div>
    <div class="credits credits-right">
      <p>Are You Ready for Jesus to Come / Redemption Draweth Nigh<br>Are You Ready for Jesus to Come – Words and Music by Roy Castellan.<br>Redemption Draweth Nigh – Words and Music by Glen and Miriam Ashford.<br>Medley Arrangement by Teodor Almaren.</p>
      <p>A Quiet Place<br>Words and Music by Lionel T. Greer. Arranged by Teodor Almaren.</p>
      <p>Midnight Cry<br>Words and Music by Carl Everett Lund and Gil Lund. Arranged by Teodor Almaren.</p>
      <p>The Holy City<br>Words by Reginald Thorne. Music by Edmund Vale. Arranged by Teodor Almaren.</p>
      <p>The Lord's Prayer<br>Words and Music by Arthur Kent Marlow. Arranged by Teodor Almaren.</p>
      <p class="studio">Recorded at Brightwater Sound, Inc.<br>Album Photos by Teodor Almaren.<br>Album Design by Nadia Ferrell</p>
    </div>
    <div class="credits thanks-left">
      <h2>SPECIAL THANKS:</h2>
      <p>To my friend Dr. Teodor Almaren– Thank you for your awe-inspiring accompaniments and encouragement for this project.</p>
      <p>To my wonderful big brother Dorian Vashti for his special song arrangements and for overseeing all the details of this project. I love you!</p>
      <p>To my loving parents for their support and unfailing encouragement– You are the best.</p>
    </div>
    <div class="credits thanks-right">
      <p>To Owen, Luis, and Mark at Brightwater Sound recording studio– Thank you for your professionalism and for working with me to make this album a success.</p>
      <h2>DEDICATION:</h2>
      <p>To God, for His mercy and love. To Him be all the glory. To Samuel Okafor, who inspired me to start this project and for his enthusiasm for our music.</p>
    </div>
  </section>

  <section class="panel panel--tray" aria-label="CD tray and disc">
    <div class="photo tray-bg" role="img" aria-label="Faded woodland background with tree trunk in soft greys and greens"></div>
    <div class="ornament tray-orn-a" role="img" aria-label="Translucent cream flourish ornament"></div>
    <div class="ornament tray-orn-b" role="img" aria-label="Translucent cream flourish ornament"></div>
    <svg class="disc-svg" width="518" height="467" viewBox="0 0 518 467" aria-hidden="true">
      <circle cx="259" cy="232" r="229" fill="var(--disc)" opacity=".93"/>
      <circle cx="259" cy="232" r="229" fill="none" stroke="#c9d9b1" stroke-width="1"/>
      <circle cx="259" cy="232" r="46" fill="#e7f0da" stroke="#cbdab6" stroke-width="1"/>
      <circle cx="259" cy="232" r="34" fill="#f3f7ec" stroke="#d3e0c0" stroke-width="1"/>
      <circle cx="259" cy="232" r="11" fill="#ffffff" stroke="#c9d6b6" stroke-width="1"/>
    </svg>
    <div class="ornament" style="left:70px;top:250px;width:280px;height:200px;background:radial-gradient(ellipse,var(--cream) 0%,rgba(243,236,200,0) 70%)" role="img" aria-label="Cream flourish ornament across the lower disc"></div>
    <div class="disc-title">
      <div class="artist-name">Corinna Vashti</div>
      <div class="album-title">Lift Up Your Lantern</div>
    </div>
  </section>

</main>
</body>
</html>
```